Brantwell Group needs a business card design

We need a new business card design using the logo recently selected in a logo competition on Pixel Forum. Our business is a consultancy specializing in aviation and energy and the winning business card design will promote an image of precision and professionalism with creativity.

Please use the logo with the name on the front of the card and use a complementary font. Make the back white with either the light grey or dark grey logo.

Target Market(s)

Senior finance and legal leaders at aviation and energy companies

Industry/Entity Type

Management Consulting

Contact Information for Business Card

Peter Haldane
President
Brantwell Group

www.brantwellgroup.example

(555) 304-6198
ph@brantwellgroup.example

Requirements
Must have
• Professional font that goes well with the logo font

```html
<!DOCTYPE html>
<html lang="en">
<head>
<meta charset="utf-8">
<title>Brantwell Group — Business Card</title>
<link href="https://fonts.googleapis.com/css2?family=Open+Sans:wght@300;400;600;700&display=swap" rel="stylesheet">
<style>
  :root {
    --backdrop: #e8e5e1;
    --grey-dark: #55585c;
    --grey-light: #b8babd;
    --brand-blue: #1d5a8e;
    --ink: #3d4045;
    --paper: #ffffff;
  }
  * { margin: 0; padding: 0; box-sizing: border-box; }
  html, body {
    width: 1200px;
    height: 913px;
    overflow: hidden;
    background: var(--backdrop);
    font-family: "Open Sans", Arial, sans-serif;
  }
  .stage {
    position: relative;
    width: 1200px;
    height: 913px;
  }
  .card {
    position: absolute;
    width: 520px;
    height: 297px;
    border-radius: 16px;
    overflow: hidden;
    box-shadow: 0 6px 18px rgba(0,0,0,0.18);
  }
  .card-front {
    left: 50px;
    top: 308px;
    background: linear-gradient(160deg, var(--grey-light) 0%, #8d8f93 45%, var(--grey-dark) 100%);
  }
  .card-back {
    left: 630px;
    top: 308px;
    background: var(--paper);
  }
  .front-shapes {
    position: absolute;
    inset: 0;
    width: 520px;
    height: 297px;
  }
  .holder {
    position: absolute;
    right: 22px;
    top: 22px;
    text-align: right;
  }
  .holder-name {
    color: var(--paper);
    font-weight: 700;
    font-size: 20px;
    line-height: 1.1;
  }
  .holder-title {
    color: var(--brand-blue);
    font-weight: 400;
    font-size: 13px;
    line-height: 1.3;
  }
  .contacts {
    position: absolute;
    right: 18px;
    top: 146px;
    list-style: none;
    text-align: right;
  }
  .contacts li {
    display: flex;
    justify-content: flex-end;
    align-items: center;
    gap: 6px;
    color: var(--ink);
    font-size: 12px;
    line-height: 19px;
    white-space: nowrap;
  }
  .contacts svg { width: 11px; height: 11px; flex: none; }
  .wordmark {
    position: absolute;
    color: var(--brand-blue);
    font-weight: 300;
    text-transform: uppercase;
    white-space: nowrap;
  }
  .wordmark-front {
    left: 34px;
    top: 200px;
    font-size: 18px;
    letter-spacing: 2px;
  }
  .wordmark-back {
    left: 0;
    right: 0;
    top: 126px;
    text-align: center;
    font-size: 32px;
    letter-spacing: 4px;
  }
</style>
</head>
<body>
<main class="stage">

  <section class="card card-front" aria-label="Business card front">
    <svg class="front-shapes" viewBox="0 0 520 297" aria-hidden="true">
      <polygon points="240,297 315,92 520,70 520,297" fill="var(--brand-blue)"/>
      <polygon points="285,297 335,112 520,112 520,297" fill="var(--paper)"/>
    </svg>

    <div class="holder">
      <p class="holder-name">Peter Haldane</p>
      <p class="holder-title">President</p>
    </div>

    <ul class="contacts">
      <li>(555) 304-6198
        <svg viewBox="0 0 12 12" aria-hidden="true"><path d="M2.5 1h2l1 3-1.3 1a6 6 0 0 0 2.8 2.8l1-1.3 3 1v2a1 1 0 0 1-1 1A9.5 9.5 0 0 1 1.5 2a1 1 0 0 1 1-1z" fill="var(--brand-blue)"/></svg>
      </li>
      <li>ph@brantwellgroup.example
        <svg viewBox="0 0 12 12" aria-hidden="true"><rect x="1" y="2.5" width="10" height="7" rx="1" fill="none" stroke="var(--brand-blue)" stroke-width="1.3"/><path d="M1.5 3l4.5 3.5L10.5 3" fill="none" stroke="var(--brand-blue)" stroke-width="1.2"/></svg>
      </li>
      <li>www.brantwellgroup.example
        <svg viewBox="0 0 12 12" aria-hidden="true"><circle cx="6" cy="6" r="5" fill="none" stroke="var(--brand-blue)" stroke-width="1.2"/><path d="M1 6h10M6 1c-2.5 3-2.5 7 0 10M6 1c2.5 3 2.5 7 0 10" fill="none" stroke="var(--brand-blue)" stroke-width="1"/></svg>
      </li>
    </ul>

    <p class="wordmark wordmark-front">Brantwell Group</p>
  </section>

  <section class="card card-back" aria-label="Business card back">
    <p class="wordmark wordmark-back">Brantwell Group</p>
  </section>

</main>
</body>
</html>
```